Electronic Music Artist needs an Album Cover

DRELL is an electronic musician from Boston, Massachusetts. He needs an album cover that captures the essence of his music. The album is called Lanterns, which represents his experiences growing up, positive and negative. He would like to see designs that involves color and creativity. Attached are some examples of artworks that DRELL likes. He also included a few of his original photos (optional to use. Using a photo will not effect his final decision!), and his logo.

Colors

Designer to choose colors to be used in the design.

Requirements
Must have
• My project must have the text "Lanterns" and "DRELL", and the logo (attached in the files). The logo should not be the main subject of the artwork. Everything must look aesthetically pleasing.
Nice to have
• It would be nice to have some sort of creative graphic design (see example album covers for reference). Also, in one of the references, there is a column on the left hand side with some text in it. That could be cool to include, but without the asian text.
Should not have
• The project should not have any other language besides English.

```html
<!DOCTYPE html>
<html lang="en">
<head>
<meta charset="utf-8">
<title>Lanterns — DRELL</title>
<link rel="stylesheet" href="https://fonts.googleapis.com/css2?family=Quicksand:wght@700&family=Syncopate:wght@700&display=swap">
<style>
  :root {
    --column-grey: rgba(110, 110, 110, 0.88);
    --column-light: rgba(150, 150, 150, 0.55);
    --title-teal: #1f4a48;
    --mark-grey: #d9d9d9;
    --artist-black: #0a0a0a;
    --scales-tan: #b89c78;
    --scales-cream: #e6d6bd;
    --proboscis-violet: #8a86b0;
    --coil-brown: #4a3a38;
    --eye-olive: #a8a43a;
    --shadow-grey: #3e3e3e;
    --leg-teal: #7c9c98;
  }
  html, body {
    margin: 0;
    padding: 0;
    width: 1200px;
    height: 1200px;
    overflow: hidden;
    background: #2e2e2e;
  }
  .cover {
    position: relative;
    width: 1200px;
    height: 1200px;
    overflow: hidden;
  }
  .cover-artwork {
    position: absolute;
    inset: 0;
    background:
      radial-gradient(circle at 1030px 360px, var(--eye-olive) 0 180px, transparent 190px),
      radial-gradient(ellipse 260px 300px at 400px 600px, var(--coil-brown) 0 60%, transparent 100%),
      radial-gradient(ellipse 200px 380px at 230px 560px, var(--proboscis-violet) 0 40%, transparent 100%),
      radial-gradient(ellipse 420px 260px at 380px 1100px, var(--leg-teal) 0 40%, transparent 100%),
      radial-gradient(ellipse 700px 620px at 750px 380px, var(--scales-cream) 0 25%, var(--scales-tan) 60%, transparent 100%),
      linear-gradient(135deg, var(--scales-tan) 0%, var(--shadow-grey) 55%, var(--scales-tan) 100%);
  }
  .title-column {
    position: absolute;
    top: 0;
    left: 0;
    width: 140px;
    height: 1200px;
    background: linear-gradient(160deg, var(--column-light) 0%, var(--column-grey) 40%, var(--column-grey) 100%);
  }
  .album-title {
    position: absolute;
    top: 28px;
    left: 26px;
    width: 90px;
    margin: 0;
    display: flex;
    flex-direction: column;
    align-items: center;
    gap: 8px;
    font-family: "Quicksand", sans-serif;
    font-weight: 700;
    font-size: 104px;
    line-height: 0.88;
    color: var(--title-teal);
  }
  .artist-mark {
    position: absolute;
    left: 32px;
    top: 1010px;
    font-family: "Quicksand", sans-serif;
    font-weight: 700;
    font-size: 46px;
    letter-spacing: 2px;
    color: var(--mark-grey);
  }
  .artist-name {
    position: absolute;
    right: 44px;
    bottom: 40px;
    margin: 0;
    font-family: "Syncopate", sans-serif;
    font-weight: 700;
    font-size: 170px;
    line-height: 0.95;
    color: var(--artist-black);
    text-align: right;
  }
  .artist-name span { display: block; }
</style>
</head>
<body>
  <main class="cover">
    <div class="cover-artwork" role="img" aria-label="Colourised close-up photograph of a moth's head: tan and cream scales, a large olive compound eye and a coiled violet-brown proboscis"></div>

    <aside class="title-column">
      <h1 class="album-title" aria-label="Lanterns">
        <span>L</span><span>A</span><span>N</span><span>T</span><span>E</span><span>R</span><span>N</span><span>S</span>
      </h1>
      <div class="artist-mark">DRELL</div>
    </aside>

    <h2 class="artist-name" aria-label="DRELL">
      <span>DR</span>
      <span>ELL</span>
    </h2>
  </main>
</body>
</html>
```